Zielgruppe
Wir sind ein Handwerksunternehemen im Bereich Elektrotechnik.
Wir sind speziell im Neubau und bei Sanierungen im Einsatz. Eh
Es wird ein passender Flyer für potentielle Neukkunden benötigt.
Der Gewinner soll uns im Anschluss zwei weitere Flyer für andere Themenbereiche erstellen!
Aufgabenstellung
Wir wünschen uns einen professionellen Flyer.
Unsere Vorgaben können gerne kreativ geändert werden.
Stockbilder evtl. passend zum Neubau / Sanierung können verwendet werden.
Bitte die Druckvorlagen beachten von Satzhaus Nord
Im Anhang sind noch zwei Flyer von anderen Unternehmen. So in der Art stellen wir uns den Flyer vor.
Im Anhang:

```html
<!DOCTYPE html>
<html lang="de">
<head>
<meta charset="utf-8">
<title>Brandt &amp; Kessler Elektrotechnik – Flyer</title>
<link rel="stylesheet" href="https://fonts.googleapis.com/css2?family=Open+Sans:ital,wght@0,400;0,600;0,700;1,600;1,700&display=swap">
<style>
:root{
  --blue:#1a8fd6;
  --blue-dark:#1473bd;
  --cyan:#1ea6dc;
  --teal:#138b8d;
  --teal-dark:#12757f;
  --grey:#bfbfbf;
  --text:#444;
  --bg:#efefef;
  --white:#fff;
}
*{box-sizing:border-box;margin:0;padding:0}
html,body{width:965px;height:1200px;overflow:hidden;background:var(--bg);font-family:"Open Sans",Arial,sans-serif;color:var(--text)}
.spread{position:absolute;left:47px;width:870px;height:555px;display:flex;box-shadow:0 6px 18px rgba(0,0,0,.18)}
.spread--outside{top:30px}
.spread--inside{top:615px}
.panel{position:relative;width:290px;height:100%;overflow:hidden;background:var(--white)}
.band{position:absolute;left:0;right:0;bottom:0;height:32px;background:var(--teal);color:var(--white);font-size:9px;font-weight:700;letter-spacing:1.2px;display:flex;align-items:center;justify-content:center;text-transform:uppercase}
.kicker{font-size:8px;font-weight:700;letter-spacing:1.2px;text-transform:uppercase;color:var(--teal)}
.headline{font-size:15px;font-weight:700;color:var(--blue);margin:24px 0 14px}
.copy{font-size:8px;line-height:1.55}
.photo{position:absolute;left:0;right:0}
/* outside */
.panel--solution{background:linear-gradient(160deg,var(--blue) 0%,var(--blue-dark) 100%);color:var(--white);padding:30px 26px}
.panel--solution .kicker{color:rgba(255,255,255,.85)}
.solution-text{font-size:11px;font-weight:600;font-style:italic;line-height:1.5;margin-top:22px}
.solution-text p+p{margin-top:12px}
.solution-mark{position:absolute;left:26px;bottom:60px;display:flex;align-items:center;gap:10px;font-size:13px;font-weight:700}
.solution-mark .dot{width:34px;height:34px;border-radius:50%;border:3px solid var(--white)}
.panel--services{padding:30px 26px}
.services-title{font-size:13px;font-weight:700;font-style:italic;color:var(--blue);margin:14px 0 12px}
.checks{list-style:none}
.checks li{display:flex;gap:7px;align-items:flex-start;font-size:8px;line-height:1.4;margin-bottom:7px}
.checks svg{flex:none;margin-top:1px}
.badge{width:120px;height:40px;border-radius:4px;background:#e6e6e6;border:1px solid #d2d2d2;margin:14px 0 18px}
.callout{font-size:10px;font-weight:700;font-style:italic;color:var(--blue);line-height:1.35}
.phone{display:flex;align-items:center;gap:7px;font-size:13px;font-weight:700;color:var(--blue);margin:10px 0 24px}
.contact-name{font-size:11px;font-weight:700;color:var(--blue);margin-bottom:8px}
.contact{font-size:8px;line-height:1.6}
.contact strong{color:var(--blue);font-weight:700}
.panel--cover{background:var(--grey)}
.cover-logo{position:absolute;left:22px;right:22px;top:0;height:150px;background:var(--white);display:flex;flex-direction:column;align-items:center;justify-content:center;gap:10px}
.wordmark{font-size:14px;font-weight:700;color:var(--blue);text-align:center;line-height:1.2}
.wordmark-dot{width:30px;height:30px;border-radius:50%;background:var(--blue)}
.cover-title{position:absolute;left:18px;top:235px}
.cover-title .main{display:inline-block;background:var(--blue);color:var(--white);font-size:13px;font-weight:700;padding:3px 6px}
.cover-title .sub{display:inline-block;margin-top:5px;background:var(--blue);color:var(--white);font-size:8px;font-weight:700;letter-spacing:1px;padding:3px 6px}
.cover-circle{position:absolute;left:160px;top:345px;width:104px;height:104px;border-radius:50%;background:var(--cyan);color:var(--white);font-size:8.5px;line-height:1.5;display:flex;align-items:center;justify-content:center;text-align:center}
.cover-circle b{font-weight:700}
/* inside */
.panel--problem{background:linear-gradient(180deg,var(--grey) 0%,#cfcfcf 70%,#e4e4e4 100%);padding:30px 26px}
.bullets{list-style:none}
.bullets li{font-size:8px;line-height:1.55;margin-bottom:10px;padding-left:8px;position:relative}
.bullets li::before{content:"·";position:absolute;left:0}
.panel--benefit{padding:30px 26px}
.benefit-lead{font-size:8px;font-weight:600;color:#333;margin:18px 0 8px}
.ticks{list-style:none}
.ticks li{display:flex;gap:8px;align-items:center;font-size:8px;font-weight:600;color:var(--blue);margin-bottom:9px}
.panel--consult{padding:30px 26px}
.quote-block{position:relative}
.quote{font-size:7.5px;line-height:1.5;color:var(--teal)}
.quote-mark{position:absolute;font-size:40px;font-weight:700;color:rgba(30,166,220,.25);line-height:1}
.quote-by{font-size:6px;line-height:1.4;color:var(--teal);margin-top:8px}
.consult-circle{position:absolute;left:150px;top:415px;width:86px;height:86px;border-radius:50%;background:var(--cyan);color:var(--white);font-size:8px;line-height:1.5;display:flex;align-items:center;justify-content:center;text-align:center}
.band--web{font-size:7.5px;letter-spacing:.4px}
</style>
</head>
<body>

<section class="spread spread--outside">
  <article class="panel panel--solution">
    <p class="kicker">Unsere Lösung</p>
    <div class="solution-text">
      <p>Uns ist wichtig, dass Bauherren pünktlich in Ihr neues Zuhause einziehen können mit maximaler Zufriedenheit an der handwerklichen Ausführung damit unsere Kunden zufriedene Auftraggeber haben.</p>
      <p>Um diesen Anspruch gerecht zu werden, setzen wir nur auf eigene ausgebildete Fachkräfte.</p>
    </div>
    <div class="solution-mark"><span class="dot"></span>Brandt &amp; Kessler</div>
    <div class="band" style="background:var(--teal-dark)"></div>
  </article>

  <article class="panel panel--services">
    <p class="kicker">Unsere Leistungen:</p>
    <h2 class="services-title">Neubau. Umbau. Sanierung.</h2>
    <ul class="checks">
      <li><svg width="10" height="10" viewBox="0 0 10 10"><circle cx="5" cy="5" r="4.3" fill="none" stroke="#1a8fd6"/><path d="M2.8 5.1l1.6 1.5 3-3.2" fill="none" stroke="#1a8fd6" stroke-width="1.1"/></svg>Beratung und Unterstützung in der Planung</li>
      <li><svg width="10" height="10" viewBox="0 0 10 10"><circle cx="5" cy="5" r="4.3" fill="none" stroke="#1a8fd6"/><path d="M2.8 5.1l1.6 1.5 3-3.2" fill="none" stroke="#1a8fd6" stroke-width="1.1"/></svg>Durchführung der Installationsarbeiten</li>
      <li><svg width="10" height="10" viewBox="0 0 10 10"><circle cx="5" cy="5" r="4.3" fill="none" stroke="#1a8fd6"/><path d="M2.8 5.1l1.6 1.5 3-3.2" fill="none" stroke="#1a8fd6" stroke-width="1.1"/></svg>Schnelle Hilfe auch bei kurzfristigen Anfragen</li>
      <li><svg width="10" height="10" viewBox="0 0 10 10"><circle cx="5" cy="5" r="4.3" fill="none" stroke="#1a8fd6"/><path d="M2.8 5.1l1.6 1.5 3-3.2" fill="none" stroke="#1a8fd6" stroke-width="1.1"/></svg>Schnelle Reaktion auf Anfragen vor und während der Projektumsetzung</li>
    </ul>
    <div class="badge" role="img" aria-label="Bewertungssiegel"></div>
    <p class="callout">Rufen Sie uns an und vereinbaren Sie ein unverbindliches Beratungsgespräch:</p>
    <p class="phone"><svg width="13" height="13" viewBox="0 0 14 14"><circle cx="7" cy="7" r="6.2" fill="none" stroke="#1a8fd6" stroke-width="1.2"/><path d="M5 3.8l1 1.8-.7.8c.4.9 1.1 1.6 2 2l.8-.7 1.8 1-.5 1.3c-2.6-.1-4.8-2.3-4.9-4.9z" fill="#1a8fd6"/></svg>040 / 31 48 72 90</p>
    <p class="contact-name">Brandt &amp; Kessler Elektrotechnik</p>
    <p class="contact"><strong>Brandt &amp; Kessler Elektrotechnik GmbH &amp; Co.KG</strong><br>Lindenweg 14 · 22991 Mühlenhagen<br>info@brandt-kessler.de · www.brandt-kessler.de<br><br>brandtkesslerelektro<br>brandt_kessler_elektro<br>www.brandt-kessler.de</p>
    <div class="band"></div>
  </article>

  <article class="panel panel--cover">
    <div class="photo" role="img" aria-label="Werkzeug, Kabel, Klemmen und Steckdose auf Betonuntergrund" style="top:0;bottom:32px;background:linear-gradient(160deg,#d6d6d6,#a9a9a9 60%,#c4c4c4)"></div>
    <div class="cover-logo"><span class="wordmark-dot"></span><p class="wordmark">Brandt &amp; Kessler Elektrotechnik</p></div>
    <div class="cover-title"><span class="main">Der Elektriker für Ihr Projekt</span><br><span class="sub">NEUBAU · UMBAU · SANIERUNG</span></div>
    <div class="cover-circle"><p>Für Ihre Anfrage<br>stehen wir unter Strom:<br><b>040 / 31 48 72 90</b></p></div>
    <div class="band">Ihr Elektriker in Mühlenhagen</div>
  </article>
</section>

<section class="spread spread--inside">
  <article class="panel panel--problem">
    <p class="kicker">Das Problem</p>
    <h2 class="headline">Sie kennen es bestimmt...</h2>
    <ul class="bullets">
      <li>Auf der Baustelle wird vermehrt kein qualifiziertes Personal von den Handwerksbetrieben eingesetzt. Wodurch keine fachgerechte Ausführung gewährleistet wird.</li>
      <li>schlechte Kommunikation auf der Baustelle oder sogar mit den Unternehmen führen schnell zu Missverständnissen.</li>
      <li>Durch eine schlechte Beratung oder Ausführung kommt es zu Nachträgen € und Verzögerungen.</li>
      <li>Keine termingerechte Fertigstellung hat unzufriedene Bauherren zur Folge.</li>
    </ul>
    <div class="photo" role="img" aria-label="Hände beim Verdrahten einer Unterputzdose" style="bottom:0;height:175px;background:linear-gradient(180deg,rgba(228,228,228,0),#d9b9a4 55%,#c99f88)"></div>
  </article>

  <article class="panel panel--benefit">
    <p class="kicker">Profitieren Sie mit uns</p>
    <h2 class="headline">Ihr Vorteil liegt auf der Hand:</h2>
    <p class="copy">Sie bekommen zufriedene Auftraggeber und haben eine hohe Planungssicherheit, weil bei uns eine termingerechte Ausführung und die Qualität der Leistung oberste Priorität hat.</p>
    <p class="benefit-lead">Mit uns haben Sie zufriedene Auftraggeber durch:</p>
    <ul class="ticks">
      <li><svg width="11" height="11" viewBox="0 0 10 10"><circle cx="5" cy="5" r="4.3" fill="none" stroke="#1a8fd6"/><path d="M2.8 5.1l1.6 1.5 3-3.2" fill="none" stroke="#1a8fd6" stroke-width="1.1"/></svg>maximale Qualität</li>
      <li><svg width="11" height="11" viewBox="0 0 10 10"><circle cx="5" cy="5" r="4.3" fill="none" stroke="#1a8fd6"/><path d="M2.8 5.1l1.6 1.5 3-3.2" fill="none" stroke="#1a8fd6" stroke-width="1.1"/></svg>hohe Planungssicherheit</li>
      <li><svg width="11" height="11" viewBox="0 0 10 10"><circle cx="5" cy="5" r="4.3" fill="none" stroke="#1a8fd6"/><path d="M2.8 5.1l1.6 1.5 3-3.2" fill="none" stroke="#1a8fd6" stroke-width="1.1"/></svg>termingerechte Ausführung</li>
    </ul>
    <div class="photo" role="img" aria-label="Portrait eines Elektrikers mit verschränkten Armen" style="bottom:32px;left:90px;right:0;height:205px;background:linear-gradient(180deg,#f4f4f4,#3a3a3a 35%,#222)"></div>
    <div class="band"></div>
  </article>

  <article class="panel panel--consult">
    <p class="kicker">Unverbindliche Beratung</p>
    <p class="copy" style="margin-top:14px">Wenn sich das für Sie interessant anhört rufen Sie uns an und vereinbaren Sie ein <b><i>unverbindliches Beratungsgespräch</i></b>:</p>
    <p class="phone" style="margin:14px 0 0 44px"><svg width="13" height="13" viewBox="0 0 14 14"><circle cx="7" cy="7" r="6.2" fill="none" stroke="#1a8fd6" stroke-width="1.2"/><path d="M5 3.8l1 1.8-.7.8c.4.9 1.1 1.6 2 2l.8-.7 1.8 1-.5 1.3c-2.6-.1-4.8-2.3-4.9-4.9z" fill="#1a8fd6"/></svg>040 / 31 48 72 90</p>
    <div class="quote-block" style="margin-top:42px;width:150px">
      <span class="quote-mark" style="left:-6px;top:-14px">“</span>
      <p class="quote">Durch die termingerechte Ausführung der Installationarbeiten von dem Team Brandt &amp; Kessler können wir immer sicherstellen unsere Projekte pünktlich an den Bauherren übergeben zu können.</p>
      <p class="quote-by">Jonas Fehrmann<br>Geschäftsführer<br>Nordlicht Dachbau</p>
    </div>
    <div class="quote-block" style="margin:-8px 0 0 70px;width:170px">
      <span class="quote-mark" style="left:-14px;top:-18px">“</span>
      <p class="quote">Uns überzeugt die saubere und gute Ausführung der Arbeit. Wir freuen uns weiterhin mit Brandt &amp; Kessler gemeinsame Projekte erfolgreich umzusetzen.</p>
      <p class="quote-by">Lukas Dreyer<br>Projektleiter<br>Hansen &amp; Voss Bau</p>
    </div>
    <div class="photo" role="img" aria-label="Portrait eines Elektrikers im Poloshirt" style="bottom:32px;left:0;width:150px;height:120px;background:linear-gradient(180deg,#f6f6f6,#4a5058 40%,#3a3f46)"></div>
    <div class="consult-circle"><p>Wir sind für Sie da!<br>Vereinbaren sie<br>jetzt Ihren Termin.</p></div>
    <div class="band band--web">info@brandt-kessler.de | www.brandt-kessler.de</div>
  </article>
</section>

</body>
</html>
```